LOS PINOS DE ARENA - EXCLUSIVE AND LUXURY REAL ESTATE PROJECT

Se trata del diseño de un mono poste grande (4 m x 2 m) o (8m x 3m) anunciando la construcción de 30 villas de lujo en un terreno en primera línea de playa en el sur de España (Cádiz).

La idea es crear expectación y transmitir lujo y exclusividad.

Target Market(s)

Clientes de alto poder adquisitivo que quieran adquirir su segunda vivienda en un entorno privilegiado a escasos pasos de una de las playas más bonitas de Cádiz.

Industry/Entity Type

REAL ESTATE

Colors

Designer to choose colors to be used in the design.

Requirements
Must have
• LOS PINOS DE ARENA as the name of the development
Nice to have
• Crear expectación con ideas del tipo: “Coming soon” o “No te lo puedes perder”

```html
<!DOCTYPE html>
<html lang="es">
<head>
<meta charset="utf-8">
<title>Los Pinos de Arena — Coming Soon</title>
<link rel="stylesheet" href="https://fonts.googleapis.com/css2?family=Oswald:wght@500;600&display=swap">
<style>
  :root {
    --page-bg: #e9ecef;
    --sand: #b08a63;
    --sea-blue: #5b78c0;
    --white: #ffffff;
    --sky-top: #8fa6d8;
    --sky-low: #c9d3ea;
    --terrace: #e6e1d9;
    --stone: #c9b79a;
  }
  * { margin: 0; padding: 0; box-sizing: border-box; }
  html, body {
    width: 1200px;
    height: 800px;
    overflow: hidden;
    background: var(--page-bg);
    font-family: "Oswald", "Arial Narrow", sans-serif;
  }
  .billboard {
    position: absolute;
    left: 50px;
    top: 125px;
    width: 1100px;
    height: 550px;
    overflow: hidden;
    background: var(--white);
    box-shadow: 0 6px 24px rgba(0,0,0,0.12);
  }
  .billboard-art {
    position: absolute;
    inset: 0;
    width: 1100px;
    height: 550px;
  }
  .project-name {
    position: absolute;
    left: 0;
    top: 0;
    width: 70px;
    height: 550px;
    display: flex;
    align-items: center;
    justify-content: center;
    writing-mode: vertical-rl;
    transform: rotate(180deg);
    color: var(--white);
    font-weight: 500;
    font-size: 34px;
    letter-spacing: 2px;
    white-space: nowrap;
  }
  .headline {
    position: absolute;
    left: 520px;
    top: 82px;
    width: 580px;
    height: 118px;
    display: flex;
    align-items: center;
    justify-content: center;
    color: var(--white);
    font-weight: 600;
    font-size: 74px;
    letter-spacing: 2px;
    white-space: nowrap;
  }
  .teaser {
    position: absolute;
    left: 755px;
    top: 245px;
    width: 240px;
    height: 240px;
    display: flex;
    align-items: center;
    justify-content: center;
    text-align: center;
    color: var(--white);
    font-weight: 500;
    font-size: 42px;
    line-height: 1.1;
    letter-spacing: 1px;
  }
</style>
</head>
<body>
  <main class="billboard">
    <svg class="billboard-art" viewBox="0 0 1100 550" xmlns="http://www.w3.org/2000/svg">
      <defs>
        <linearGradient id="villa-photo-tones" x1="0" y1="0" x2="0" y2="1">
          <stop offset="0" stop-color="var(--sky-top)"/>
          <stop offset="0.35" stop-color="var(--sky-low)"/>
          <stop offset="0.55" stop-color="var(--stone)"/>
          <stop offset="0.75" stop-color="var(--terrace)"/>
          <stop offset="1" stop-color="#f2efea"/>
        </linearGradient>
      </defs>

      <rect class="villa-photo" x="70" y="0" width="620" height="550"
            fill="url(#villa-photo-tones)" role="img"
            aria-label="Photograph of a modern white luxury villa with glass walls and a sunny terrace"/>

      <path class="content-panel" fill="var(--white)"
            d="M640,0 H1100 V550 H535 C550,460 600,400 605,300 C610,200 590,110 640,0 Z"/>

      <path class="sand-ribbon" fill="none" stroke="var(--sand)" stroke-width="40"
            d="M648,-20 C592,110 612,200 606,300 C600,400 552,460 530,570"/>

      <polygon class="headline-band" fill="var(--sea-blue)"
               points="480,82 1100,82 1100,200 515,200"/>

      <circle class="teaser-badge" cx="875" cy="365" r="120" fill="var(--sand)"/>

      <rect class="name-band" x="0" y="0" width="70" height="550" fill="var(--sand)"/>
    </svg>

    <h1 class="project-name">LOS PINOS DE ARENA</h1>
    <p class="headline">COMING SOON</p>
    <p class="teaser">NO TE LO<br>PUEDES<br>PERDER</p>
  </main>
</body>
</html>
```